3 Holiday typography sets (10x19)

I have 6 phrases that I need designed as 3 coordinated sets on a 10x19 canvas size. The 2 phrases in each set should coordinate, but each of the 3 sets can have their own look.

Set #1 - southern/casual feel
Merry Christmas to y’all and to y’all a goodnight
Christmas feels warmer in the South

Set #2 - traditional/classic feel
There’s snowplace like home (snowflakes/snowman)
Hearts come home for Christmas

Set #3 - fun/whimsical feel
Christmas calories don’t count (cookies)
He sees you when you’re eating

The accent element ideas in parentheses are optional and I am open to other design/accent elements. All 3 sets need to be on a white background.

Target Market(s)

women 25-55

Colors
ec1f27
9bcb3c
cadf82
7f7f7f
ffffff

Requirements
Must have
• coordinated feel per set, but each set can have its own look/font/etc

```html
<!DOCTYPE html>
<html lang="en">
<head>
<meta charset="utf-8">
<title>Snowplace Like Home</title>
<link href="https://fonts.googleapis.com/css2?family=Alice&family=Arvo:wght@700&family=Josefin+Slab:wght@400&family=Didact+Gothic&family=Kaushan+Script&display=swap" rel="stylesheet">
<style>
  :root {
    --red: #ec1f27;
    --green: #9bcb3c;
    --light-green: #cadf82;
    --grey: #7f7f7f;
    --snow: #e9e9e9;
    --white: #ffffff;
  }
  * { margin: 0; padding: 0; box-sizing: border-box; }
  html, body { width: 1200px; height: 2280px; overflow: hidden; background: var(--white); }
  .poster { position: relative; width: 1200px; height: 2280px; background: var(--white); overflow: hidden; }

  .word { position: absolute; white-space: nowrap; line-height: 1; }
  .word--there { left: 270px; top: 96px; font: 400 122px "Alice", serif; color: var(--red); }
  .word--is { left: 604px; top: 232px; font: italic 400 104px "Alice", serif; color: var(--red); }
  .word--snowplace { left: 180px; top: 366px; font: 700 132px "Arvo", serif; color: var(--green); letter-spacing: 2px; }
  .word--like-home { left: 108px; top: 540px; font: 400 226px "Josefin Slab", serif; color: var(--grey); line-height: 0.97; }
  .word--hearts { left: 556px; top: 1330px; font: 400 150px "Alice", serif; color: var(--red); }
  .word--come-home { left: 32px; top: 1592px; font: 400 156px "Didact Gothic", sans-serif; color: var(--grey); }
  .word--for { left: 476px; top: 1752px; font: 400 218px "Didact Gothic", sans-serif; color: var(--green); }
  .word--christmas { left: 196px; top: 1970px; font: 400 200px "Kaushan Script", cursive; color: var(--red); }

  .art { position: absolute; }
  .art--snowman { left: 720px; top: 560px; width: 400px; height: 420px; border-radius: 46% 46% 50% 50%; background: radial-gradient(circle at 45% 40%, var(--white), var(--snow) 70%, #d8d8d8); }
  .art--hearts { left: 176px; top: 1200px; width: 330px; height: 340px; border-radius: 50% 50% 46% 46%; background: radial-gradient(circle at 40% 35%, #f4545a, var(--red) 70%); }
  .art--bells { left: 816px; top: 1500px; width: 344px; height: 320px; border-radius: 48%; background: radial-gradient(circle at 50% 30%, var(--green), var(--light-green) 55%, #ef6a55 85%); }

  .flake { position: absolute; border-radius: 50%; }
  .flake--red { background: radial-gradient(circle, rgba(236,31,39,0.75), rgba(236,31,39,0.15) 70%, transparent 72%); }
  .flake--green { background: radial-gradient(circle, rgba(155,203,60,0.7), rgba(155,203,60,0.15) 70%, transparent 72%); }
  .flake--pale { background: radial-gradient(circle, rgba(202,223,130,0.9), rgba(202,223,130,0.25) 70%, transparent 72%); }
</style>
</head>
<body>
<main class="poster">
  <div class="flake flake--red" style="left:64px;top:56px;width:120px;height:120px" role="img" aria-label="Red snowflake ornament"></div>
  <div class="flake flake--red" style="left:860px;top:60px;width:220px;height:220px" role="img" aria-label="Red snowflake ornament"></div>
  <div class="flake flake--green" style="left:216px;top:240px;width:64px;height:64px" role="img" aria-label="Green snowflake ornament"></div>
  <div class="flake flake--green" style="left:740px;top:208px;width:140px;height:140px" role="img" aria-label="Green snowflake ornament"></div>
  <div class="flake flake--green" style="left:880px;top:300px;width:60px;height:60px" role="img" aria-label="Green snowflake ornament"></div>
  <div class="flake flake--green" style="left:72px;top:480px;width:72px;height:72px" role="img" aria-label="Green snowflake ornament"></div>
  <div class="flake flake--red" style="left:608px;top:608px;width:40px;height:40px" role="img" aria-label="Red snowflake ornament"></div>
  <div class="flake flake--green" style="left:572px;top:720px;width:72px;height:72px" role="img" aria-label="Green snowflake ornament"></div>
  <div class="flake flake--red" style="left:972px;top:980px;width:108px;height:108px" role="img" aria-label="Red snowflake ornament"></div>
  <div class="flake flake--green" style="left:288px;top:1048px;width:124px;height:124px" role="img" aria-label="Green snowflake ornament"></div>
  <div class="flake flake--green" style="left:608px;top:1140px;width:132px;height:132px" role="img" aria-label="Green snowflake ornament"></div>
  <div class="flake flake--pale" style="left:928px;top:1180px;width:184px;height:184px" role="img" aria-label="Pale green snowflake ornament"></div>
  <div class="flake flake--green" style="left:100px;top:1828px;width:132px;height:132px" role="img" aria-label="Green snowflake ornament"></div>
  <div class="flake flake--green" style="left:912px;top:1848px;width:72px;height:72px" role="img" aria-label="Green snowflake ornament"></div>
  <div class="flake flake--red" style="left:1000px;top:1900px;width:120px;height:120px" role="img" aria-label="Red snowflake ornament"></div>

  <p class="word word--there">There</p>
  <p class="word word--is">is</p>
  <p class="word word--snowplace">SNOWPLACE</p>
  <p class="word word--like-home">like<br>home</p>
  <div class="art art--snowman" role="img" aria-label="Illustration of a snowman with top hat and red scarf"></div>

  <div class="art art--hearts" role="img" aria-label="Illustration of two red hearts"></div>
  <p class="word word--hearts">Hearts</p>
  <p class="word word--come-home">come home</p>
  <div class="art art--bells" role="img" aria-label="Illustration of two Christmas bells with holly"></div>
  <p class="word word--for">for</p>
  <p class="word word--christmas">Christmas</p>
</main>
</body>
</html>
```